Business Cards for Orvanta LLC

We need business cards for a new company called “Orvanta LLC”. This is a technology process improvement company providing a comprehensive assessment of the technology used to run their business. The documentation and review process delivers the visibility and reassurance they need to protect their business and plan for the future. The product is called “Systems Mapwork”. Our primary target is small-medium size businesses, with the deliverables going to the decision maker. We would like to see the designs use the color blue. Our tag line is PROTECT YOUR BUSINESS · TAKE CONTROL OF IT.

Industry/Entity Type

Business

Contact Information for Business Card

Tag line should be on back of card - it does not have to be upper case.

Requirements
Must have
• Please use information when laying out card:
• Name: Gareth Pellham
• Title: Partner
• Phone Number: (844)555-0172
• Email: gareth@orvantallc-example.com
• Website: http://orvantallc-example.com

```html
<!DOCTYPE html>
<html lang="en">
<head>
<meta charset="utf-8">
<title>Business Card – Orvanta LLC</title>
<link href="https://fonts.googleapis.com/css2?family=Open+Sans:wght@400;600;700&display=swap" rel="stylesheet">
<style>
  :root {
    --page-bg: #e6eaef;
    --brand-blue: #0b4c9c;
    --brand-blue-deep: #083f85;
    --panel-light: #f4f5f7;
    --panel-mid: #d8dce2;
    --divider-grey: #4f555c;
    --text-white: #ffffff;
    --text-soft: #c9d4e2;
    --icon-bg: #c9d4e2;
  }
  * { margin: 0; padding: 0; box-sizing: border-box; }
  html, body {
    width: 1200px; height: 970px; overflow: hidden;
    background: var(--page-bg);
    font-family: "Open Sans", Arial, sans-serif;
  }
  .canvas { position: relative; width: 1200px; height: 970px; }
  .card {
    position: absolute; left: 120px; top: 210px;
    width: 960px; height: 550px;
    border-radius: 22px; overflow: hidden;
    box-shadow: 0 18px 40px rgba(20, 40, 70, 0.22);
  }
  .card-art { position: absolute; inset: 0; }
  .holder { position: absolute; left: 50px; top: 88px; color: var(--text-white); }
  .holder-name { font-size: 32px; font-weight: 600; line-height: 1; }
  .holder-title { font-size: 24px; font-weight: 400; line-height: 1.05; }
  .contacts { position: absolute; left: 50px; top: 276px; list-style: none; }
  .contact {
    display: flex; align-items: center; gap: 12px;
    height: 34px; font-size: 23px; color: var(--text-soft);
  }
  .contact-icon { width: 26px; height: 26px; flex: none; }
  .tagline {
    position: absolute; left: 50px; top: 392px;
    font-size: 22px; font-weight: 600; letter-spacing: 0.8px;
    line-height: 32px; color: var(--text-soft); text-transform: uppercase;
  }
  .brand-name {
    position: absolute; left: 470px; right: 0; top: 288px;
    text-align: center; font-size: 52px; font-weight: 700;
    color: var(--brand-blue); letter-spacing: 1px;
  }
</style>
</head>
<body>
<main class="canvas">
  <section class="card" aria-label="Business card for Orvanta LLC">
    <svg class="card-art" viewBox="0 0 960 550" width="960" height="550" aria-hidden="true">
      <defs>
        <linearGradient id="panelLight" x1="0" y1="0" x2="1" y2="1">
          <stop offset="0" stop-color="var(--panel-light)"/>
          <stop offset="1" stop-color="var(--panel-mid)"/>
        </linearGradient>
        <linearGradient id="panelBlue" x1="0" y1="0" x2="1" y2="1">
          <stop offset="0" stop-color="var(--brand-blue)"/>
          <stop offset="1" stop-color="var(--brand-blue-deep)"/>
        </linearGradient>
      </defs>
      <rect class="light-panel" width="960" height="550" fill="url(#panelLight)"/>
      <path class="divider-shade" d="M488 0 Q364 275 488 550 L500 550 Q388 275 500 0 Z" fill="var(--divider-grey)" opacity="0.75"/>
      <path class="blue-panel" d="M0 0 H488 Q364 275 488 550 H0 Z" fill="url(#panelBlue)"/>
      <circle class="notch" cx="0" cy="109" r="24" fill="var(--page-bg)"/>
    </svg>

    <div class="holder">
      <p class="holder-name">Gareth Pellham</p>
      <p class="holder-title">Partner</p>
    </div>

    <ul class="contacts">
      <li class="contact">
        <svg class="contact-icon" viewBox="0 0 26 26" aria-hidden="true">
          <rect width="26" height="26" rx="3" fill="var(--icon-bg)"/>
          <path d="M9 6 L12 6 L13 10 L11 11.5 Q12.5 15 15 16 L16.5 14 L20 15 L20 18 Q18 21 14 19 Q8 16 6.5 10 Q6 7 9 6 Z" fill="var(--brand-blue)"/>
        </svg>
        <span>(844)555-0172</span>
      </li>
      <li class="contact">
        <svg class="contact-icon" viewBox="0 0 26 26" aria-hidden="true">
          <rect width="26" height="26" rx="3" fill="var(--icon-bg)"/>
          <rect x="5" y="8" width="16" height="11" fill="none" stroke="var(--brand-blue)" stroke-width="1.6"/>
          <path d="M5 8 L13 14 L21 8 M5 19 L11 13 M21 19 L15 13" fill="none" stroke="var(--brand-blue)" stroke-width="1.4"/>
        </svg>
        <span>gareth@orvantallc-example.com</span>
      </li>
      <li class="contact">
        <svg class="contact-icon" viewBox="0 0 26 26" aria-hidden="true">
          <rect width="26" height="26" rx="3" fill="var(--icon-bg)"/>
          <circle cx="13" cy="13" r="8" fill="none" stroke="var(--brand-blue)" stroke-width="1.4"/>
          <ellipse cx="13" cy="13" rx="3.5" ry="8" fill="none" stroke="var(--brand-blue)" stroke-width="1.2"/>
          <path d="M5 13 H21 M6.5 9 H19.5 M6.5 17 H19.5" stroke="var(--brand-blue)" stroke-width="1.1"/>
        </svg>
        <span>orvantallc-example.com</span>
      </li>
    </ul>

    <p class="tagline">Protect your business<br>take control of it.</p>

    <p class="brand-name">Orvanta LLC</p>
  </section>
</main>
</body>
</html>
```